Brightwell Galley Hour Podcast

We need a Podcast Cover design that is compatible with Apple Podcasts, Spotify, etc. In this podcast, we interview the real movers & shakers in the foodservice industry who cut through the noise to get to the top.

```html
<!DOCTYPE html>
<html lang="en">
<head>
<meta charset="utf-8">
<title>Brightwell Galley Hour Podcast Cover</title>
<link rel="stylesheet" href="https://fonts.googleapis.com/css2?family=Roboto:wght@400&family=Italiana&display=swap">
<style>
  :root {
    --amber-light: #e9c77a;
    --amber: #b8893e;
    --bronze: #6e5326;
    --olive-dark: #3a3520;
    --navy: #142238;
    --ink: #05070b;
    --title-ink: #0a0a0a;
    --cream: #ffffff;
  }
  html, body {
    margin: 0;
    padding: 0;
    width: 1200px;
    height: 1200px;
    overflow: hidden;
    background: var(--ink);
  }
  .cover {
    position: relative;
    width: 1200px;
    height: 1200px;
    overflow: hidden;
  }
  .cover-photo {
    position: absolute;
    inset: 0;
    background:
      radial-gradient(ellipse 420px 620px at 830px 620px, rgba(20,34,56,0.95) 0%, rgba(20,34,56,0.6) 55%, rgba(20,34,56,0) 100%),
      radial-gradient(ellipse 700px 500px at 300px 300px, var(--amber-light) 0%, var(--amber) 45%, rgba(110,83,38,0.4) 80%, rgba(58,53,32,0) 100%),
      radial-gradient(ellipse 300px 500px at 1150px 350px, rgba(184,137,62,0.8) 0%, rgba(110,83,38,0) 100%),
      linear-gradient(180deg, var(--bronze) 0%, var(--olive-dark) 55%, var(--ink) 100%);
  }
  .cover-shade {
    position: absolute;
    left: 0;
    right: 0;
    bottom: 0;
    height: 620px;
    background: linear-gradient(180deg, rgba(5,7,11,0) 0%, rgba(5,7,11,0.75) 45%, rgba(5,7,11,0.97) 100%);
  }
  .show-title {
    position: absolute;
    right: 654px;
    top: 162px;
    margin: 0;
    font-family: "Roboto", sans-serif;
    font-weight: 400;
    font-size: 70px;
    line-height: 1.12;
    text-align: right;
    color: var(--title-ink);
    letter-spacing: 0.5px;
  }
  .host {
    position: absolute;
    left: 22px;
    top: 690px;
    margin: 0;
    color: var(--cream);
    font-family: "Italiana", serif;
    font-weight: 400;
  }
  .host-with {
    display: block;
    margin-left: 252px;
    font-size: 27px;
    letter-spacing: 6px;
    line-height: 1;
  }
  .host-first,
  .host-last {
    display: block;
    font-size: 250px;
    line-height: 0.82;
    letter-spacing: -4px;
  }
  .host-last {
    margin-top: 14px;
  }
</style>
</head>
<body>
  <main class="cover">
    <div class="cover-photo" role="img" aria-label="Photo of the smiling host in a navy blazer and light blue shirt, seated at a warmly lit restaurant bar"></div>
    <div class="cover-shade"></div>
    <h1 class="show-title">Brightwell<br>Galley Hour</h1>
    <p class="host">
      <span class="host-with">with</span>
      <span class="host-first">Theo,</span>
      <span class="host-last">Marchand</span>
    </p>
  </main>
</body>
</html>
```